TradoMarkly.com
Stationary and Business Cards
Professional
Martin Chalwick
President / CEO
712 Westbrook Blvd
Suite 2300
Atlanta, GA 30318
mchalwick@tradomarkly-example.com
www.tradomarkly-example.com
I want the logo and tagline on the back of the business card. A marketplace connecting wholesale buyers and sellers.

```html
<!DOCTYPE html>
<html lang="en">
<head>
<meta charset="utf-8">
<title>TradoMarkly.com Stationery</title>
<link href="https://fonts.googleapis.com/css2?family=Questrial&display=swap" rel="stylesheet">
<style>
:root{
  --green:#2f9a3f;
  --blue:#1d3d8f;
  --ink:#3a3a3a;
  --muted:#8a8a8a;
  --paper:#ffffff;
  --bg:#e9e6e1;
  --rule:#c9c9c9;
}
*{box-sizing:border-box;margin:0;padding:0}
html,body{width:1200px;height:935px;overflow:hidden;background:var(--bg);font-family:"Questrial",sans-serif;color:var(--ink)}
.canvas{position:relative;width:1200px;height:935px}
.sheet{position:absolute;background:var(--paper);box-shadow:0 4px 14px rgba(0,0,0,.18)}
.brand{font-family:"Questrial",sans-serif;color:var(--blue);font-weight:400;letter-spacing:.5px;line-height:1;white-space:nowrap}
.brand-dot{display:inline-block;border-radius:50%;background:var(--green);vertical-align:middle;margin-right:8px}
.band{position:absolute;left:0;right:0;background:var(--green);color:#fff;white-space:nowrap}

/* fax */
.fax{left:38px;top:55px;width:470px;height:810px}
.fax .brand{position:absolute;left:40px;top:50px;font-size:30px}
.fax-title{position:absolute;left:40px;top:130px;font-size:40px;letter-spacing:2px;font-weight:400}
.fax-fields{position:absolute;left:40px;top:215px;width:380px;list-style:none;font-size:13px}
.fax-fields li{display:flex;height:40px;align-items:flex-end;border-bottom:1px solid var(--rule);padding-bottom:4px}
.fax-checks{position:absolute;left:40px;top:410px;display:flex;gap:40px;font-size:13px;color:var(--muted)}
.fax-checks span::before{content:"";display:inline-block;width:11px;height:11px;border:1px solid var(--muted);margin-right:8px;vertical-align:-1px}
.fax .band{bottom:55px;height:55px;padding:12px 40px;font-size:11px;line-height:1.5}

/* letterhead */
.letterhead{left:200px;top:100px;width:485px;height:800px}
.letterhead .brand{position:absolute;left:45px;top:70px;font-size:32px}
.letterhead .faint{position:absolute;left:45px;top:330px;font-size:78px;color:var(--blue);opacity:.08}
.letterhead .band{bottom:46px;height:66px;padding:11px 28px;display:flex;gap:16px;font-size:9.5px;line-height:1.5}
.band .sep{width:1px;background:rgba(255,255,255,.6)}

/* envelope */
.envelope{left:525px;top:355px;width:645px;height:380px;background:none;box-shadow:none}
.envelope svg.flap{position:absolute;left:0;top:0}
.envelope .flap-brand{position:absolute;left:0;right:0;top:18px;text-align:center;font-size:18px;color:#fff}
.envelope .body{position:absolute;left:0;top:62px;width:645px;height:318px;background:var(--paper);box-shadow:0 4px 14px rgba(0,0,0,.18)}
.envelope .body .brand{position:absolute;left:40px;top:65px;font-size:40px}
.envelope .band{top:220px;height:52px;display:flex;align-items:center;justify-content:space-between;padding:0 30px;font-size:12px}
.envelope .addr{line-height:1.45;font-size:11px}
.tagline{font-size:15px}

/* cards */
.card{width:320px;height:110px;border-radius:8px;overflow:hidden}
.card-front{left:850px;top:68px}
.card-front .brand{position:absolute;left:18px;top:16px;font-size:24px}
.card-front .person{position:absolute;right:18px;top:18px;text-align:right;font-size:11px;white-space:nowrap}
.card-front .person small{display:block;color:var(--muted);font-size:9px}
.card-front .addr{position:absolute;left:18px;top:54px;font-size:8.5px;line-height:1.35;color:var(--muted);white-space:nowrap}
.card-front .web{position:absolute;right:18px;top:62px;text-align:right;font-size:8.5px;line-height:1.4;color:var(--muted);white-space:nowrap}
.card-front .band{bottom:0;height:12px}
.card-back{left:850px;top:230px;background:var(--green)}
.card-back .brand{position:absolute;left:0;right:0;top:26px;text-align:center;font-size:30px;color:#fff}
.card-back .tagline{position:absolute;left:0;right:0;bottom:16px;text-align:center;font-size:11px;color:#fff}
</style>
</head>
<body>
<main class="canvas">

  <section class="sheet fax" aria-label="Fax cover sheet">
    <div class="brand"><span class="brand-dot" style="width:12px;height:12px"></span>TradoMarkly</div>
    <h1 class="fax-title">FAX</h1>
    <ul class="fax-fields">
      <li>To:</li><li>Fax:</li><li>Phone:</li><li>Re:</li>
    </ul>
    <div class="fax-checks"><span>Urgent</span><span>For Review</span></div>
    <div class="band">712 Westbrook Blvd<br>Suite 2300, Atlanta, GA 30318</div>
  </section>

  <section class="sheet letterhead" aria-label="Letterhead">
    <div class="brand"><span class="brand-dot" style="width:12px;height:12px"></span>TradoMarkly</div>
    <div class="brand faint" aria-hidden="true">TradoMarkly</div>
    <div class="band">
      <div>712 Westbrook Blvd<br>Suite 2300<br>Atlanta, GA 30318</div>
      <div class="sep"></div>
      <div>T: 404-555-0142<br>F: 404-555-0187<br>C: 404-555-0163</div>
      <div class="sep"></div>
      <div>E: mchalwick@tradomarkly-example.com<br>W: www.tradomarkly-example.com</div>
    </div>
  </section>

  <section class="sheet envelope" aria-label="Envelope">
    <svg class="flap" width="645" height="70" viewBox="0 0 645 70" aria-hidden="true">
      <path d="M0 70 L40 8 Q45 0 55 0 L590 0 Q600 0 605 8 L645 70 Z" fill="var(--green)"/>
    </svg>
    <div class="brand flap-brand">TradoMarkly</div>
    <div class="body">
      <div class="brand"><span class="brand-dot" style="width:14px;height:14px"></span>TradoMarkly</div>
      <div class="band">
        <div class="addr">712 Westbrook Blvd<br>Suite 2300, Atlanta, GA 30318</div>
        <div class="tagline">A marketplace connecting wholesale buyers and sellers.</div>
      </div>
    </div>
  </section>

  <section class="sheet card card-front" aria-label="Business card front">
    <div class="brand"><span class="brand-dot" style="width:9px;height:9px"></span>TradoMarkly</div>
    <div class="person">Martin Chalwick<small>President / CEO</small></div>
    <div class="addr">712 Westbrook Blvd<br>Suite 2300<br>Atlanta, GA 30318</div>
    <div class="web">mchalwick@tradomarkly-example.com<br>www.tradomarkly-example.com</div>
    <div class="band"></div>
  </section>

  <section class="sheet card card-back" aria-label="Business card back">
    <div class="brand">TradoMarkly</div>
    <div class="tagline">A marketplace connecting wholesale buyers and sellers.</div>
  </section>

</main>
</body>
</html>
```